Steady-Point Snack Vending Needs a Promotional Flyer

Design a one page, one sided 8 1/2" x 11" flyer that can be handed out to potential customers. Please keep printing efficiencies in mind. See attached old flyers and company website (steadypointvend.com) for reference of services. I have also attached our current logo.

```html
<!DOCTYPE html>
<html lang="en">
<head>
<meta charset="utf-8">
<title>Steady-Point Snack Vending Flyer</title>
<link href="https://fonts.googleapis.com/css2?family=Jost:wght@400;500;600;700&display=swap" rel="stylesheet">
<style>
  :root {
    --sky: #4db8e6;
    --navy: #243746;
    --ink: #1c1c1c;
    --paper: #ffffff;
    --panel: #e4e6e8;
    --rule: #8e969c;
    --backdrop: #4f5d62;
    --photo-a: #16324a;
    --photo-b: #6fd2f2;
  }
  * { box-sizing: border-box; margin: 0; padding: 0; }
  html, body { width: 1200px; height: 1017px; overflow: hidden; }
  body { background: var(--backdrop); font-family: "Jost", sans-serif; color: var(--ink); }

  .flyer {
    position: absolute; left: 230px; top: 30px;
    width: 740px; height: 958px;
    background: var(--paper); overflow: hidden;
  }
  .swoosh { position: absolute; left: 0; top: 0; width: 740px; height: 958px; }

  .hero-photo {
    position: absolute; left: 40px; top: 100px; width: 290px; height: 290px;
    border-radius: 50%; border: 6px solid var(--paper);
    background: radial-gradient(circle at 50% 55%, var(--photo-b) 0%, #2f7fa6 35%, var(--photo-a) 80%);
  }

  .brand {
    position: absolute; left: 440px; top: 70px; width: 270px;
    display: flex; align-items: center; gap: 12px;
  }
  .brand-mark { width: 34px; height: 34px; background: var(--navy); flex: none; }
  .brand-name { font-weight: 700; font-size: 21px; line-height: 1.05; color: var(--navy); text-transform: uppercase; }
  .brand-rule { position: absolute; left: 430px; top: 162px; width: 290px; height: 3px; background: var(--navy); }

  .menu-panel { position: absolute; left: 440px; top: 170px; width: 270px; height: 610px; }
  .menu-panel svg { position: absolute; inset: 0; }
  .menu-content { position: relative; padding: 26px 26px 0 26px; }
  .menu-title { font-size: 13px; font-weight: 600; line-height: 1.3; text-transform: uppercase; margin-bottom: 14px; }
  .menu-list { list-style: none; }
  .menu-list li {
    font-size: 12px; line-height: 18.5px; border-bottom: 1px solid var(--rule);
    white-space: nowrap;
  }
  .menu-note { font-size: 10px; font-weight: 700; text-transform: uppercase; line-height: 1.3; margin-top: 16px; }

  .headline { position: absolute; left: 40px; top: 432px; }
  .headline-lead { font-size: 40px; font-weight: 700; color: var(--ink); line-height: 1; letter-spacing: -0.5px; }
  .headline-name { font-size: 46px; font-weight: 700; color: var(--sky); line-height: 1.05; letter-spacing: -0.5px; }

  .reasons { position: absolute; left: 44px; top: 550px; width: 370px; list-style: none; }
  .reasons li {
    position: relative; padding-left: 18px; font-size: 14.5px; font-weight: 500;
    line-height: 1.3; margin-bottom: 8px;
  }
  .reasons li::before {
    content: ""; position: absolute; left: 2px; top: 7px; width: 6px; height: 6px;
    border-radius: 50%; background: var(--ink);
  }

  .address-band {
    position: absolute; left: 0; top: 862px; width: 400px; height: 56px;
    background: var(--ink); color: var(--paper);
    font-size: 12px; font-weight: 600; font-style: normal; text-transform: uppercase; line-height: 1.35;
    padding: 11px 0 0 44px;
  }
  .phone-tab {
    position: absolute; left: 380px; top: 818px; width: 360px; height: 100px;
    background: var(--sky); border-top-left-radius: 22px;
    display: flex; align-items: center; padding-left: 24px;
    font-size: 29px; font-weight: 700; color: var(--ink); white-space: nowrap;
  }
  .base-strip { position: absolute; left: 0; top: 928px; width: 740px; height: 14px; background: var(--sky); }
</style>
</head>
<body>
<main class="flyer">
  <svg class="swoosh" viewBox="0 0 740 958" aria-hidden="true">
    <path d="M0 0 H330 C210 90 150 230 140 330 C130 390 60 420 0 428 Z" fill="var(--sky)"/>
    <path d="M330 0 H352 C232 92 172 232 162 332 C152 405 72 440 0 448 V428 C60 420 130 390 140 330 C150 230 210 90 330 0 Z" fill="var(--navy)"/>
  </svg>

  <div class="hero-photo" role="img" aria-label="Photo of a lit snack vending machine"></div>

  <header class="brand">
    <span class="brand-mark"></span>
    <span class="brand-name">Steady-Point Snack Vending</span>
  </header>
  <div class="brand-rule"></div>

  <section class="menu-panel">
    <svg viewBox="0 0 270 610" preserveAspectRatio="none" aria-hidden="true">
      <path d="M0 0 H270 V590 l-10 12 -10 -12 -10 12 -10 -12 -10 12 -10 -12 -10 12 -10 -12 -10 12 -10 -12 -10 12 -10 -12 -10 12 -10 -12 -10 12 -10 -12 -10 12 -10 -12 -10 12 -10 -12 -10 12 -10 -12 -10 12 -10 -12 -10 12 -10 -12 Z" fill="var(--panel)"/>
    </svg>
    <div class="menu-content">
      <h2 class="menu-title">We offer a wide variety of coffee options to our customers:</h2>
      <ul class="menu-list">
        <li>Hillcrest Roasters</li>
        <li>Snow Bear</li>
        <li>Columbian</li>
        <li>Maxwood Hall Filter Packs</li>
        <li>Maxwood Hall Master Blend</li>
        <li>Ridgeway House Blend</li>
        <li>Ridgeway French Roast</li>
        <li>Foldwell Flavor Filter</li>
        <li>Stanwick House Blend</li>
        <li>Starline French Roast (Available)</li>
        <li>Cream Canisters</li>
        <li>Liquid Creamers</li>
        <li>French Vanilla Liquid Creamers</li>
        <li>Sugar Canisters</li>
        <li>Sugar Packets</li>
        <li>Sweet Lite</li>
        <li>Even Sweetener</li>
        <li>Linden's Tea Bags</li>
        <li>Snow Valley Hot Cocoa Mix</li>
        <li>Foam &amp; Paper Coffee Cups</li>
        <li>Stirrers</li>
        <li>Coffee Pots</li>
        <li>Coffee Filters</li>
      </ul>
      <p class="menu-note">There are other specialty<br>items available upon request</p>
    </div>
  </section>

  <h1 class="headline">
    <span class="headline-lead">WHY CHOOSE</span><br>
    <span class="headline-name">STEADY-POINT?</span>
  </h1>

  <ul class="reasons">
    <li>Our Warehouse Is Just Minutes Away So We Can Get There Quickly If A Problem Should Arise.</li>
    <li>We Are A Small Company That Is Big On Service</li>
    <li>We Are Owner-operators So We Truly Care About Our Customers</li>
    <li>We Are Also Trained To Fix Many Problems On The Spot</li>
    <li>We Will Supply Machines To Your Facility</li>
    <li>Customer Service Is Our Priority</li>
    <li>Your Employees Can Choose What Types Of Snacks and Drinks They Would Like To See In The Machines.</li>
    <li>We Take Pride In What We Do!</li>
  </ul>

  <div class="phone-tab">PHONE (630) 555-0148</div>
  <address class="address-band">1480 Meadowline Ave, Unit 210,<br>Fairbrook, IL, 60599</address>
  <div class="base-strip"></div>
</main>
</body>
</html>
```